Redesign of business card for Birchline Mechanical

We are looking for a new design for our business cards for Birchline Mechanical. We are a plumbing & HVAC construction company, operating on the West Coast of Canada and USA. Logo attached.
Industry/Entity Type
Construction - Plumbing & HVAC
Contact Information for Business Card
Name, address, phone numbers, email, website address
Look and feel
Each slider illustrates characteristics of the customer's brand and the style your logo design should communicate.

```html
<!DOCTYPE html>
<html lang="en">
<head>
<meta charset="utf-8">
<title>Birchline Mechanical – Business Card</title>
<link href="https://fonts.googleapis.com/css2?family=Poppins:wght@400;600&display=swap" rel="stylesheet">
<style>
  :root {
    --backdrop: #e8e8e8;
    --card-light: #ffffff;
    --card-dark: #353535;
    --ink: #353535;
    --ink-strong: #2b2b2b;
    --rule: #1e1e1e;
    --paper-text: #ffffff;
  }
  * { margin: 0; padding: 0; box-sizing: border-box; }
  html, body {
    width: 1200px; height: 510px; overflow: hidden;
    background: var(--backdrop);
    font-family: "Poppins", sans-serif;
    color: var(--ink);
  }
  .canvas { position: relative; width: 1200px; height: 510px; }
  .card {
    position: absolute; top: 120px; width: 472px; height: 270px;
    box-shadow: 0 4px 14px rgba(0,0,0,0.28);
  }
  .card--front { left: 113px; background: var(--card-light); }
  .card--back { left: 614px; background: var(--card-dark); }

  .brand {
    position: absolute; display: flex; align-items: center; gap: 8px;
    font-weight: 600; white-space: nowrap;
  }
  .brand__square { display: block; background: currentColor; flex: none; }
  .card--front .brand {
    right: 26px; top: 62px; font-size: 13px; color: var(--ink);
  }
  .card--front .brand__square { width: 11px; height: 11px; }
  .card--back .brand {
    left: 0; right: 0; top: 118px; justify-content: center;
    font-size: 24px; letter-spacing: 0.5px; color: var(--paper-text);
  }
  .card--back .brand__square { width: 20px; height: 20px; }

  .person { position: absolute; left: 30px; top: 147px; }
  .person__name { font-size: 19px; font-weight: 600; color: var(--ink-strong); line-height: 1.15; }
  .person__role { font-size: 13px; font-weight: 400; line-height: 1.3; }

  .divider {
    position: absolute; left: 30px; top: 193px; width: 408px; height: 1px;
    background: var(--rule);
  }

  .contacts {
    position: absolute; left: 28px; top: 201px; list-style: none;
    font-size: 13px; line-height: 17px;
  }
  .contacts li { display: flex; align-items: center; gap: 7px; }
  .contacts svg { width: 12px; height: 12px; fill: var(--ink); flex: none; }

  .address {
    position: absolute; right: 26px; top: 218px; text-align: right;
    font-size: 13px; line-height: 17px; font-style: normal;
  }
</style>
</head>
<body>
<div class="canvas">
  <section class="card card--front">
    <div class="brand"><span class="brand__square"></span>Birchline Mechanical</div>

    <div class="person">
      <p class="person__name">Daniel Harlow</p>
      <p class="person__role">Managing Director</p>
    </div>

    <div class="divider"></div>

    <ul class="contacts">
      <li>
        <svg viewBox="0 0 24 24" aria-hidden="true"><path d="M6.6 2.5l3 3.4-1.8 2.6c1.2 3 3.6 5.4 6.6 6.6l2.6-1.8 3.4 3-1.9 3.5C10.5 20 4 13.5 3.1 4.4z"/></svg>
        <span>206-555-0148</span>
      </li>
      <li>
        <svg viewBox="0 0 24 24" aria-hidden="true"><path d="M2 6l10 6 10-6v12H2z"/><path d="M2 4h20v1.3L12 11 2 5.3z"/></svg>
        <span>dan@birchlinemech.com</span>
      </li>
      <li>
        <svg viewBox="0 0 24 24" aria-hidden="true"><path d="M12 2a10 10 0 100 20 10 10 0 000-20zm0 1.8c1 1 1.9 2.6 2.3 4.7H9.7C10.1 6.4 11 4.8 12 3.8zM4.2 10.3h4.9a17 17 0 000 3.4H4.2a7.9 7.9 0 010-3.4zm10.7 0h4.9a7.9 7.9 0 010 3.4h-4.9a17 17 0 000-3.4zm-4 0h2.2a15 15 0 010 3.4h-2.2a15 15 0 010-3.4zm-1.2 5.2h4.6c-.4 2.1-1.3 3.7-2.3 4.7-1-1-1.9-2.6-2.3-4.7z"/></svg>
        <span>www.birchlinemech.com</span>
      </li>
    </ul>

    <address class="address">
      421 address line goes here<br>
      45452, country name
    </address>
  </section>

  <section class="card card--back">
    <div class="brand"><span class="brand__square"></span>BIRCHLINE MECHANICAL</div>
  </section>
</div>
</body>
</html>
```